brisknest

i want to ues this logo and the same colors used on the business card

cleaning & service

Industry/Entity Type

Business

Contact Information for Business Card

Font styles to use
Serif
Sans Serif
Decorative
Script

Colors
add136
0692cd
000000
5c5c5c
fbfbfb

Requirements
Must have
• cleaning things

```html
<!DOCTYPE html>
<html lang="en">
<head>
<meta charset="utf-8">
<title>brisknest business card</title>
<link href="https://fonts.googleapis.com/css2?family=Roboto:wght@300;400;500&display=swap" rel="stylesheet">
<style>
  :root {
    --green: #add136;
    --green-deep: #82b83a;
    --blue: #0692cd;
    --blue-light: #2fa8e0;
    --ink: #000000;
    --text-dark: #1f1f1f;
    --grey: #5c5c5c;
    --paper: #fbfbfb;
    --backdrop: #d9d9d9;
  }
  html, body {
    margin: 0;
    width: 1200px;
    height: 923px;
    overflow: hidden;
    background: var(--backdrop);
    font-family: "Roboto", Arial, sans-serif;
  }
  .card {
    position: absolute;
    left: 100px;
    top: 175px;
    width: 1000px;
    height: 572px;
    background: var(--paper);
    overflow: hidden;
    box-shadow: 0 10px 30px rgba(0,0,0,0.18);
  }
  .card__waves {
    position: absolute;
    inset: 0;
    width: 100%;
    height: 100%;
  }
  .wave--green { fill: var(--green-deep); }
  .wave--white { fill: var(--paper); }
  .wave--blue { fill: var(--blue-light); }
  .brand {
    position: absolute;
    left: 120px;
    top: 48px;
    width: 300px;
    display: flex;
    flex-direction: column;
    align-items: center;
    gap: 18px;
  }
  .brand__art {
    width: 200px;
    height: 200px;
    background: linear-gradient(160deg, var(--blue) 0%, #5aa9c9 45%, var(--green) 100%);
    opacity: 0.85;
  }
  .brand__name {
    font-size: 50px;
    font-weight: 500;
    line-height: 1;
    color: var(--blue);
    letter-spacing: 0.5px;
  }
  .contact {
    position: absolute;
    right: 70px;
    top: 150px;
    text-align: right;
  }
  .contact__name {
    font-size: 30px;
    font-weight: 400;
    color: var(--text-dark);
    margin: 0;
  }
  .contact__role {
    font-size: 21px;
    font-weight: 300;
    color: var(--paper);
    margin: 2px 0 0;
  }
  .contact__lines {
    margin-top: 56px;
    font-size: 20px;
    color: var(--text-dark);
    line-height: 36px;
  }
  .contact__line {
    display: flex;
    justify-content: flex-end;
    align-items: center;
    gap: 12px;
  }
  .contact__icon {
    width: 18px;
    height: 18px;
    fill: var(--paper);
  }
</style>
</head>
<body>
  <article class="card">
    <svg class="card__waves" viewBox="0 0 1000 572" preserveAspectRatio="none" aria-hidden="true">
      <path class="wave--green" d="M0 500 C 260 500, 440 470, 520 300 C 600 130, 720 60, 1000 50 L1000 572 L0 572 Z"/>
      <path class="wave--white" d="M290 520 C 420 500, 500 440, 560 300 C 630 140, 720 80, 800 62 C 710 100, 650 170, 590 310 C 530 450, 430 510, 290 520 Z"/>
      <path class="wave--blue" d="M0 455 C 200 455, 380 430, 445 300 C 440 360, 330 470, 0 490 Z"/>
    </svg>

    <div class="brand">
      <div class="brand__art" role="img" aria-label="Cleaning illustration: broom sweeping beside sparkling clean buildings"></div>
      <span class="brand__name">brisknest</span>
    </div>

    <div class="contact">
      <p class="contact__name">Your Name</p>
      <p class="contact__role">Owner</p>
      <div class="contact__lines">
        <div class="contact__line">
          <span>(123) 123-1234</span>
          <svg class="contact__icon" viewBox="0 0 24 24"><path d="M6.6 10.8a15.1 15.1 0 0 0 6.6 6.6l2.2-2.2c.3-.3.7-.4 1-.2 1.1.4 2.3.6 3.6.6.6 0 1 .4 1 1V20c0 .6-.4 1-1 1C10.6 21 3 13.4 3 4c0-.6.4-1 1-1h3.5c.6 0 1 .4 1 1 0 1.3.2 2.5.6 3.6.1.3 0 .7-.2 1z"/></svg>
        </div>
        <div class="contact__line">
          <span>hello@brisknest.com</span>
          <svg class="contact__icon" viewBox="0 0 24 24"><path d="M2 5h20v14H2z M3.5 6.5 12 13l8.5-6.5" fill="var(--paper)" stroke="var(--green-deep)" stroke-width="1.4"/></svg>
        </div>
      </div>
    </div>
  </article>
</body>
</html>
```